R & T Welford Carpet & Gutter Cleaning

We clean carpets and have an environmentally friendly gutter machine that cleans out the guttering leaving no mess
Phone 0402718395
or 0413862047

Industry/Entity Type

Business

```html
<!DOCTYPE html>
<html lang="en">
<head>
<meta charset="utf-8">
<title>R &amp; T Welford Carpet &amp; Gutter Cleaning – Business Card</title>
<link rel="stylesheet" href="https://fonts.googleapis.com/css2?family=Exo+2:wght@800&family=Open+Sans:wght@400;700&display=swap">
<style>
  :root {
    --page-bg: #e9e6e1;
    --card-white: #ffffff;
    --brand-blue: #1a6a9a;
    --band-red: #e31e24;
    --card-black: #000000;
    --text-white: #ffffff;
  }
  * { box-sizing: border-box; margin: 0; padding: 0; }
  html, body {
    width: 1200px;
    height: 816px;
    overflow: hidden;
    background: var(--page-bg);
  }
  .canvas {
    position: relative;
    width: 1200px;
    height: 816px;
    display: flex;
    align-items: center;
    justify-content: center;
  }
  .card {
    position: relative;
    width: 1120px;
    height: 684px;
    border-radius: 44px;
    overflow: hidden;
    background: var(--card-white);
    box-shadow: 0 6px 18px rgba(0,0,0,0.12);
  }
  .card__brand {
    position: absolute;
    left: 110px;
    top: 118px;
    font-family: "Exo 2", sans-serif;
    font-weight: 800;
    color: var(--brand-blue);
    text-transform: uppercase;
    line-height: 1;
  }
  .card__brand-name {
    display: block;
    font-size: 104px;
    letter-spacing: 2px;
  }
  .card__brand-trade {
    display: block;
    margin-top: 10px;
    font-size: 46px;
    letter-spacing: 1px;
  }
  .card__services {
    position: absolute;
    left: 0;
    top: 338px;
    width: 100%;
    height: 46px;
    background: var(--band-red);
    color: var(--text-white);
    font-family: "Open Sans", sans-serif;
    font-weight: 700;
    font-size: 27px;
    text-transform: uppercase;
  }
  .card__service {
    position: absolute;
    top: 50%;
    transform: translate(-50%, -50%);
    white-space: nowrap;
  }
  .card__service--carpet { left: 330px; }
  .card__service-divider { left: 528px; font-weight: 400; }
  .card__service--gutter { left: 800px; }
  .card__contact {
    position: absolute;
    left: 0;
    top: 384px;
    width: 100%;
    height: 300px;
    background: var(--card-black);
    color: var(--text-white);
    font-family: "Open Sans", sans-serif;
  }
  .card__call {
    position: absolute;
    left: 292px;
    top: 88px;
    font-size: 50px;
    font-weight: 400;
  }
  .card__phones {
    position: absolute;
    left: 470px;
    top: 44px;
    list-style: none;
  }
  .card__phone {
    display: flex;
    align-items: center;
    gap: 16px;
    height: 66px;
    font-size: 38px;
    font-weight: 700;
    letter-spacing: 1px;
  }
  .card__phone-icon {
    width: 40px;
    height: 40px;
    flex: none;
  }
</style>
</head>
<body>
<main class="canvas">
  <article class="card">
    <h1 class="card__brand">
      <span class="card__brand-name">R &amp; T Welford</span>
      <span class="card__brand-trade">Carpet &amp; Gutter Cleaning</span>
    </h1>

    <div class="card__services">
      <span class="card__service card__service--carpet">Carpet Cleaning</span>
      <span class="card__service card__service-divider">I</span>
      <span class="card__service card__service--gutter">Gutter Machine Cleaning</span>
    </div>

    <section class="card__contact">
      <span class="card__call">Call</span>
      <ul class="card__phones">
        <li class="card__phone">
          <svg class="card__phone-icon" viewBox="0 0 40 40" aria-hidden="true">
            <rect width="40" height="40" rx="7" fill="#ffffff"/>
            <path d="M14 8 h5 v7 h-3 q-1 5 0 10 h3 v7 h-5 q-5 -12 0 -24 z" fill="#000000"/>
          </svg>
          0402718395
        </li>
        <li class="card__phone">
          <svg class="card__phone-icon" viewBox="0 0 40 40" aria-hidden="true">
            <rect width="40" height="40" rx="7" fill="#ffffff"/>
            <path d="M14 8 h5 v7 h-3 q-1 5 0 10 h3 v7 h-5 q-5 -12 0 -24 z" fill="#000000"/>
          </svg>
          0413862047
        </li>
      </ul>
    </section>
  </article>
</main>
</body>
</html>
```